New audiology website PSD design only - guaranteed

We need a clean and attractive website to replace an existing Audiology (hearing technology) website which will be wordpress based.
The current website is: http://pelmorahearing.com.au
They have a new logo and colors which you can find at www.quodel.net/temp/plh2018.pdf
We will no longer have a web shop in the new website
To enter the competition, we only need a sample of the home page.
The winning design will be asked to produce 2 standard page template alternatives as well (based on the winning home page design, but for a standard page layout)
The winning design must provide any photos used
We want a clean, credible site but with some warmth
Target Market(s)
All ages but needs to include the elderly
Industry/Entity Type
Medical And Science
Number of Pages Required
3 page
Look and feel
Each slider illustrates characteristics of the customer's brand and the style your logo design should communicate.

```html
<!DOCTYPE html>
<html lang="en">
<head>
<meta charset="utf-8">
<title>Pelmora Hearing – Home</title>
<link rel="stylesheet" href="https://fonts.googleapis.com/css2?family=Raleway:wght@300;400;600;700&family=Roboto:wght@300;400;500;700&display=swap">
<style>
:root{
  --orange:#f07424;
  --ink:#2b2b2b;
  --text:#6f6f6f;
  --muted:#9a9a9a;
  --line:#e6e6e6;
  --dark:#13181c;
  --black:#050505;
  --panel:#f4f4f5;
  --white:#ffffff;
}
*{box-sizing:border-box;margin:0;padding:0}
html,body{width:1200px;height:2381px;overflow:hidden;background:var(--white)}
body{position:relative;font-family:'Roboto',sans-serif;color:var(--text)}
.abs{position:absolute}
.rule{position:absolute;height:3px;width:30px;background:var(--orange)}

/* top bar */
.topbar{left:88px;top:0;width:1045px;height:22px;border-bottom:1px solid var(--line);font-size:9px;color:var(--text)}
.social{display:flex;gap:14px;position:absolute;left:216px;top:6px}
.social i{display:block;width:9px;height:9px;border-radius:50%;background:#8a8a8a}
.topinfo{position:absolute;right:0;top:5px;display:flex;gap:18px;align-items:center}
.topinfo span{display:flex;align-items:center;gap:5px}
.topinfo svg{width:9px;height:9px}
.cart{color:var(--orange)}

/* nav */
.nav{left:88px;top:22px;width:1045px;height:39px}
.logo{position:absolute;left:176px;top:9px;display:flex;align-items:center;gap:6px;font-family:'Raleway',sans-serif;font-weight:700;font-size:17px;color:var(--ink)}
.logo i{display:block;width:20px;height:20px;border-radius:50%;background:var(--orange)}
.menu{position:absolute;left:358px;top:14px;display:flex;gap:19px;font-size:9px;color:var(--ink)}
.menu .active{position:relative}
.menu .active:after{content:"";position:absolute;left:0;right:0;top:20px;height:2px;background:var(--orange)}
.search{position:absolute;right:90px;top:13px;font-size:9px;color:var(--muted);display:flex;align-items:center;gap:6px}

/* hero */
.hero{left:88px;top:61px;width:1045px;height:461px;background:linear-gradient(90deg,#f1efec 0%,#f6f4f1 35%,#e3c3cd 55%,#d7b7a6 75%,#eae7e4 100%)}
.hero-text{position:absolute;left:173px;top:150px}
.hero-title{font-family:'Raleway',sans-serif;font-weight:700;font-size:33px;line-height:38px}
.hero-title .accent{color:var(--orange)}
.hero-title .strong{color:var(--ink)}
.hero-sub{font-size:13px;color:var(--ink);margin-top:8px}
.btn{display:inline-block;background:var(--orange);color:var(--white);font-size:8px;font-weight:500;text-transform:uppercase;text-align:center;letter-spacing:.3px}
.hero .btn{position:absolute;left:3px;top:109px;width:72px;height:25px;line-height:25px}
.appt-tab{position:absolute;left:173px;bottom:0;width:144px;height:20px;background:#2b2f33;color:var(--white);font-size:9px;line-height:20px;padding-left:9px}
.appt-tab svg{position:absolute;right:10px;top:7px}

/* welcome */
.welcome{left:88px;top:522px;width:1045px;height:366px;text-align:center}
.welcome .kicker{position:absolute;top:24px;width:100%;font-family:'Raleway',sans-serif;font-weight:700;font-size:15px;line-height:18px;color:var(--ink)}
.welcome .title{position:absolute;top:40px;width:100%;font-family:'Raleway',sans-serif;font-weight:300;font-size:23px;line-height:26px;color:var(--ink)}
.welcome .rule{left:507px;top:72px}
.welcome .intro{position:absolute;left:250px;top:86px;width:550px;font-size:8.5px;line-height:15px}
.feature{position:absolute;top:166px;width:200px;text-align:center}
.feature .ring{width:66px;height:66px;margin:0 auto}
.feature h3{font-family:'Raleway',sans-serif;font-weight:600;font-size:12px;color:var(--ink);margin-top:28px}
.feature p{font-size:8px;line-height:14px;margin-top:8px;padding:0 20px}

/* appointment */
.appointment{left:88px;top:888px;width:1045px;height:264px;background:var(--dark);color:#b5b8ba}
.appointment h2{position:absolute;left:218px;top:62px;font-family:'Raleway',sans-serif;font-weight:600;font-size:15px;color:var(--white)}
.appointment .rule{left:218px;top:86px}
.appointment p{position:absolute;left:218px;top:104px;width:230px;font-size:8px;line-height:14px}
.field{position:absolute;width:168px;height:22px;border:1px solid #2c3237;font-size:8px;line-height:20px;padding-left:4px;color:#b5b8ba}
.appointment .btn{position:absolute;left:483px;top:174px;width:68px;height:26px;line-height:26px}

/* team */
.team{left:88px;top:1152px;width:1045px;height:464px;text-align:center}
.team .kicker{position:absolute;top:28px;width:100%;font-family:'Raleway',sans-serif;font-weight:700;font-size:14px;color:var(--ink)}
.team .title{position:absolute;top:42px;width:100%;font-family:'Raleway',sans-serif;font-weight:300;font-size:22px;color:var(--ink)}
.card{position:absolute;top:110px;width:195px;height:295px;background:var(--panel)}
.card .photo{height:142px}
.card .band{height:42px;background:var(--orange);color:var(--white);padding-top:7px}
.card .name{font-family:'Raleway',sans-serif;font-weight:700;font-size:12px}
.card .role{font-size:7px;margin-top:3px}
.hours{width:160px;margin:10px auto 0;font-size:7.5px;color:var(--ink);text-align:left}
.hours div{display:flex;justify-content:space-between;height:19px;border-bottom:1px solid var(--line);line-height:18px}
.hours div:last-child{border-bottom:none}
.card .profile{display:block;width:70px;height:21px;margin:6px auto 0;border:1px solid var(--orange);font-size:6.5px;line-height:19px;color:var(--ink);text-transform:uppercase}
.dots{position:absolute;top:426px;left:494px;display:flex;gap:5px}
.dots i{display:block;width:7px;height:7px;border-radius:50%;background:#d8d8d8}
.dots i:first-child{background:var(--orange)}

/* testimonials */
.testimonials{left:88px;top:1616px;width:1045px;height:328px;background:var(--panel);text-align:center}
.testimonials .kicker{position:absolute;top:22px;width:100%;font-family:'Raleway',sans-serif;font-weight:700;font-size:14px;color:var(--ink)}
.testimonials .title{position:absolute;top:36px;width:100%;font-family:'Raleway',sans-serif;font-weight:300;font-size:22px;color:var(--ink)}
.avatar{position:absolute;left:487px;top:112px;width:70px;height:70px;border-radius:50%;background:linear-gradient(160deg,#e7c9a0,#d6a7a0 60%,#eadfe1)}
.arrow{position:absolute;top:140px}
.quote{position:absolute;left:300px;top:200px;width:390px;font-size:8px;line-height:16px}
.qmark{position:absolute;font-family:'Raleway',sans-serif;font-weight:700;font-size:18px;color:var(--orange)}
.testimonials .name{position:absolute;top:276px;width:100%;font-family:'Raleway',sans-serif;font-weight:600;font-size:13px;color:var(--ink)}

/* location */
.location{left:88px;top:1944px;width:1045px;height:251px;background:linear-gradient(100deg,#ecebe8 0%,#e5e7e2 40%,#eee3d4 70%,#ebe9e6 100%)}
.contact-panel{position:absolute;left:174px;top:0;width:191px;height:251px;background:var(--orange);color:var(--white);padding:28px 0 0 28px}
.contact-panel h4{font-family:'Raleway',sans-serif;font-weight:700;font-size:12px;text-transform:uppercase}
.contact-panel p{font-size:7.5px;line-height:11px;margin-top:6px}
.contact-panel .h2{margin-top:14px}
.crow{display:flex;align-items:center;gap:8px;font-size:7.5px;margin-top:10px}
.contact-panel .meet{position:absolute;left:28px;top:192px;width:114px;height:29px;background:var(--white);color:var(--orange);font-size:7px;font-weight:700;text-align:center;line-height:29px;text-transform:uppercase}
.pin{position:absolute;left:508px;top:152px}

/* footer */
.footer{left:88px;top:2195px;width:1045px;height:150px;background:var(--black);color:#7d7d7d}
.fcol{position:absolute;top:36px;font-size:7.5px;line-height:11.5px}
.fcol h5{font-family:'Raleway',sans-serif;font-weight:700;font-size:10px;color:var(--white);margin-bottom:14px}
.news-input{width:144px;height:21px;background:var(--white);color:var(--muted);font-size:7px;line-height:21px;padding-left:6px;margin-top:8px}
.news-btn{width:78px;height:21px;line-height:21px;margin-top:8px;background:var(--orange);color:var(--white);font-size:9px;font-weight:700;text-align:center}
.bottombar{left:88px;top:2345px;width:1045px;height:36px;background:var(--black);border-top:1px solid #1d1d1d;font-size:7px;color:#7d7d7d}
.bottombar .copy{position:absolute;left:193px;top:14px}
.bottombar .social{left:717px;top:13px;gap:8px}
.bottombar .social i{width:8px;height:8px;background:#cfcfcf}
</style>
</head>
<body>

<div class="abs topbar">
  <div class="social"><i></i><i></i><i></i></div>
  <div class="topinfo">
    <span><svg viewBox="0 0 10 10"><circle cx="5" cy="5" r="4" fill="none" stroke="#f07424" stroke-width="1.2"/><path d="M5 2.6V5h2" fill="none" stroke="#f07424" stroke-width="1.1"/></svg>Monday to Friday 9am to 5pm</span>
    <span><svg viewBox="0 0 10 10"><path d="M2 1l2 2-1 1.5a6 6 0 0 0 2.5 2.5L7 6l2 2-1.2 1.2C5 9 1 5 0.8 2.2z" fill="#f07424"/></svg>(02) 5550 1482 , 5550 7316</span>
    <span><svg viewBox="0 0 10 10"><circle cx="5" cy="3.2" r="2.2" fill="none" stroke="#f07424"/><path d="M1 9.5a4 4 0 0 1 8 0" fill="none" stroke="#f07424"/></svg>My Account &nbsp;|</span>
    <span class="cart"><svg viewBox="0 0 10 10"><path d="M1.5 3h7l-.7 6H2.2z M3.5 3V2a1.5 1.5 0 0 1 3 0v1" fill="none" stroke="#f07424"/></svg>0.00</span>
  </div>
</div>

<div class="abs nav">
  <div class="logo"><i></i>Pelmora Hearing</div>
  <nav class="menu">
    <span class="active">Your Hearing</span><span>Hearing Aids</span><span>Musicians</span><span>Doctors Information</span><span>About Us</span><span>Products</span><span>Contact us</span>
  </nav>
  <div class="search"><svg width="10" height="10" viewBox="0 0 10 10"><circle cx="4" cy="4" r="3" fill="none" stroke="#9a9a9a" stroke-width="1.2"/><path d="M6.3 6.3L9 9" stroke="#9a9a9a" stroke-width="1.3"/></svg>Search</div>
</div>

<section class="abs hero" role="img" aria-label="Photo of a smiling audiologist in a white coat with a young girl looking through an otoscope">
  <div class="hero-text">
    <h1 class="hero-title"><span class="accent">A New Hearing</span><br><span class="strong">Health Experience</span></h1>
    <div class="hero-sub">Check Out Our Services!</div>
    <span class="btn">Check out</span>
  </div>
  <div class="appt-tab">Make an Appointment<svg width="8" height="5" viewBox="0 0 8 5"><path d="M0 5L4 0l4 5z" fill="#fff"/></svg></div>
</section>

<section class="abs welcome">
  <div class="kicker">Welcome to</div>
  <h2 class="title">Pelmora Hearing</h2>
  <span class="rule"></span>
  <p class="intro">Pelmora Hearing is an independently owned and managed professional audiology clinic. Our Audiologists are health-care professionals specialising in diagnosing, treating and monitoring everything to do with hearing and balance. At Pelmora Hearing we work closely with Ear, Nose and Throat specialists to ensure you receive the highest standards of medical care.</p>

  <div class="feature" style="left:167px">
    <svg class="ring" viewBox="0 0 66 66"><circle cx="33" cy="33" r="31" fill="none" stroke="#b9a49a" stroke-width="1.5"/><circle cx="33" cy="33" r="26" fill="none" stroke="#b9a49a" stroke-width="1"/><path d="M22 38v-6a11 11 0 0 1 22 0v6" fill="none" stroke="#b9a49a" stroke-width="1.6"/><rect x="20" y="34" width="5" height="9" rx="2" fill="none" stroke="#b9a49a" stroke-width="1.5"/><rect x="41" y="34" width="5" height="9" rx="2" fill="none" stroke="#b9a49a" stroke-width="1.5"/></svg>
    <h3>Audiological Evaluation</h3>
    <p>The first step begins with a proper audiological evaluation. The right hearing aid selection is made once we thoroughly understand your hearing loss and lifestyle needs.</p>
  </div>
  <div class="feature" style="left:407px">
    <svg class="ring" viewBox="0 0 66 66"><circle cx="33" cy="33" r="31" fill="none" stroke="#b9a49a" stroke-width="1.5"/><circle cx="33" cy="33" r="26" fill="none" stroke="#b9a49a" stroke-width="1"/><circle cx="33" cy="33" r="13" fill="none" stroke="#b9a49a" stroke-width="1.5"/><path d="M27 33l4.5 4.5L40 29" fill="none" stroke="#b9a49a" stroke-width="1.8"/></svg>
    <h3>Hearing Aid Selection</h3>
    <p>The next step is to assist you in helping you make the appropriate hearing aid selection according to your technological needs as well as your financial needs.</p>
  </div>
  <div class="feature" style="left:666px">
    <svg class="ring" viewBox="0 0 66 66"><circle cx="33" cy="33" r="31" fill="none" stroke="#b9a49a" stroke-width="1.5"/><circle cx="33" cy="33" r="26" fill="none" stroke="#b9a49a" stroke-width="1"/><path d="M27 30a7 7 0 0 1 14 0c0 5-5 6-5 10a3 3 0 0 1-6 0" fill="none" stroke="#b9a49a" stroke-width="1.6"/><path d="M31 30a3 3 0 0 1 6 0c0 2-2 3-2 4" fill="none" stroke="#b9a49a" stroke-width="1.3"/></svg>
    <h3>Custom Fitting Process</h3>
    <p>Lastly, our audiologists will listen intently to your feedback and then use all of our expertise and knowledge to ensure that your hearing aids are properly adjusted.</p>
  </div>
</section>

<section class="abs appointment">
  <h2>Make an Appointment</h2>
  <span class="rule"></span>
  <p>Simply dummy text of the printing and typesetting industry Lorem Ipsum has been the industry's standard dummy text ever unknown printer took.Simply dummy text of the printin and typesetting dustry's standard.</p>
  <div class="field" style="left:482px;top:82px">Name*</div>
  <div class="field" style="left:658px;top:82px">E-mail</div>
  <div class="field" style="left:482px;top:114px">Phone</div>
  <div class="field" style="left:658px;top:114px">MAN</div>
  <div class="field" style="left:482px;top:146px">Department</div>
  <div class="field" style="left:658px;top:146px">Date</div>
  <span class="btn">Submit</span>
</section>

<section class="abs team">
  <div class="kicker">Pelmora Hearing</div>
  <h2 class="title">Team</h2>

  <article class="card" style="left:202px">
    <div class="photo" role="img" aria-label="Photo of a female audiologist at work" style="background:linear-gradient(135deg,#b9b4ad,#5f6c82 60%,#2f3f5c)"></div>
    <div class="band"><div class="name">Dr. Elena Marsh</div><div class="role">Doctor Post</div></div>
    <div class="hours"><div><span>Monday - Friday</span><span>9:00 - 17:00</span></div><div><span>Saturday</span><span>10:00 - 16:00</span></div><div><span>Sunday</span><span>12:00 - 14:00</span></div></div>
    <span class="profile">Read Profile</span>
  </article>
  <article class="card" style="left:424px">
    <div class="photo" role="img" aria-label="Black and white portrait photo of the practice manager" style="background:linear-gradient(135deg,#e8e8e8,#9a9a9a 55%,#d9d9d9)"></div>
    <div class="band"><div class="name">Owen Castell</div><div class="role">Director/Practice Manager</div></div>
    <div class="hours"><div><span>Monday - Friday</span><span>9:00 - 17:00</span></div><div><span>Saturday</span><span>10:00 - 16:00</span></div><div><span>Sunday</span><span>12:00 - 14:00</span></div></div>
    <span class="profile">Read Profile</span>
  </article>
  <article class="card" style="left:646px">
    <div class="photo" role="img" aria-label="Portrait photo of a female doctor in a white coat" style="background:linear-gradient(135deg,#cfe0ea,#e9d9c2 55%,#f1f4f6)"></div>
    <div class="band"><div class="name">Dr. Elena Marsh</div><div class="role">Doctor Post</div></div>
    <div class="hours"><div><span>Monday - Friday</span><span>9:00 - 17:00</span></div><div><span>Saturday</span><span>10:00 - 16:00</span></div><div><span>Sunday</span><span>12:00 - 14:00</span></div></div>
    <span class="profile">Read Profile</span>
  </article>

  <div class="dots"><i></i><i></i><i></i><i></i><i></i></div>
</section>

<section class="abs testimonials">
  <div class="kicker">What</div>
  <h2 class="title">Patients Say</h2>
  <svg class="arrow" style="left:470px" width="8" height="12" viewBox="0 0 8 12"><path d="M6.5 1L2 6l4.5 5" fill="none" stroke="#2b2b2b" stroke-width="2"/></svg>
  <div class="avatar" role="img" aria-label="Round portrait photo of the patient"></div>
  <svg class="arrow" style="left:576px" width="8" height="12" viewBox="0 0 8 12"><path d="M1.5 1L6 6l-4.5 5" fill="none" stroke="#2b2b2b" stroke-width="2"/></svg>
  <span class="qmark" style="left:280px;top:194px">&ldquo;</span>
  <p class="quote">There are many variations of passages of Lorem Ipsum available, but the majority have suffered alteration in some form, by injected humour, or randomised words which don't look even slightly believable. If you are going to use a passage of Lorem Ipsum, you need to be sure there isn't anything embarrassing hidden</p>
  <span class="qmark" style="left:660px;top:246px">&rdquo;</span>
  <div class="name">Corin Hale</div>
</section>

<section class="abs location" role="img" aria-label="Street map showing the clinic location">
  <div class="contact-panel">
    <h4>Address</h4>
    <p>Suite 2, 48 Larkfield Road,<br>Hollin Vale, NSW 2099</p>
    <h4 class="h2">Contact Details</h4>
    <div class="crow"><svg width="9" height="9" viewBox="0 0 10 10"><path d="M2 1l2 2-1 1.5a6 6 0 0 0 2.5 2.5L7 6l2 2-1.2 1.2C5 9 1 5 0.8 2.2z" fill="#fff"/></svg>(02) 5550 1482</div>
    <div class="crow"><svg width="10" height="8" viewBox="0 0 10 8"><rect x=".5" y=".5" width="9" height="7" fill="none" stroke="#fff"/><path d="M.5.5L5 4.5 9.5.5" fill="none" stroke="#fff"/></svg>info@pelmorahearing.com.au</div>
    <span class="meet">Meet Now</span>
  </div>
  <svg class="pin" width="16" height="22" viewBox="0 0 16 22"><path d="M8 0a8 8 0 0 1 8 8c0 6-8 14-8 14S0 14 0 8a8 8 0 0 1 8-8z" fill="#e0332b"/><circle cx="8" cy="8" r="3" fill="#8e1712"/></svg>
</section>

<footer class="abs footer">
  <div class="fcol" style="left:194px"><h5>Quick Links</h5>Your Hearing<br>Hearing Aids<br>Musicians<br>Doctors Information<br>About Us<br>Products<br>Contact us</div>
  <div class="fcol" style="left:379px"><h5>Our Services</h5>Ear Whitening<br>Ear Treatment<br>Ear Xpress<br>Ear Treatment<br>Ear Whitening<br>Ear Whitening<br>Ear Treatment</div>
  <div class="fcol" style="left:538px"><h5>Opening Hours</h5>Monday : 9:00 - 17:00<br>Tuesday : 9:00 - 17:00<br>Wednesday : 9:00 - 17:00<br>Thursday : 9:00 - 17:00<br>Friday : 9:00 - 17:00<br>Saturday : 10:00 - 16:00<br>Sunday : 12:00 - 14:00</div>
  <div class="fcol" style="left:709px"><h5>Newsletter Sign Up</h5>Stay updated with latest news<br>from our clinic team
    <div class="news-input">Email</div>
    <div class="news-btn">Submit</div>
  </div>
</footer>

<div class="abs bottombar">
  <span class="copy">&copy; Pelmora Hearing 2017</span>
  <div class="social"><i></i><i></i><i></i><i></i><i></i></div>
</div>

</body>
</html>
```